Business Card

Designs by L&M Renata Kowalczyk Signature Collection business card
Looking for a modern, classic and timeless business card for our jewelry company

Front of card should be a, all purple solid color for the background and white lettering like the attached document.

On the front of card:
Designs by L&M
Renata Kowalczyk Signature Collection
One of A Kind Designs for you!

Renata Fairbury
Owner

On the back on card
Email: LMDesigns27@postvela.com
Facebook: https://www.facepage-example.com/DesignsbyLMRenataandHolly
Twitter:
https://chirpline-example.com/DesignsbyLM27
Instagram: http://picstream-example.com/DesignsbyLMjewelry

Industry/Entity Type

Business

```html
<!DOCTYPE html>
<html lang="en">
<head>
<meta charset="utf-8">
<title>Designs by L&amp;M – Business Card</title>
<link rel="stylesheet" href="https://fonts.googleapis.com/css2?family=Questrial&display=swap">
<style>
  :root {
    --page-bg: #1c1c1e;
    --card-back: #2a2829;
    --card-front: #6a3f9c;
    --card-front-deep: #5a3288;
    --band: rgba(255, 255, 255, 0.09);
    --ink: #f2eff5;
    --ink-soft: #c9bfd6;
    --ink-muted: #a99cbb;
  }
  * { margin: 0; padding: 0; box-sizing: border-box; }
  html, body {
    width: 1200px;
    height: 997px;
    overflow: hidden;
    background: var(--page-bg);
    font-family: "Questrial", "Century Gothic", sans-serif;
    color: var(--ink);
  }
  .stage {
    position: relative;
    width: 1200px;
    height: 997px;
  }
  .card {
    position: absolute;
    width: 560px;
    height: 320px;
    border-radius: 18px;
    box-shadow: 0 18px 40px rgba(0, 0, 0, 0.55);
    overflow: hidden;
  }

  /* Back of card */
  .card--back {
    left: 80px;
    top: 150px;
    background: var(--card-back);
  }
  .brand {
    text-align: center;
  }
  .brand__name {
    font-size: 24px;
    letter-spacing: 7px;
    text-transform: uppercase;
  }
  .brand__name::before {
    content: "";
    display: inline-block;
    width: 12px;
    height: 12px;
    border-radius: 50%;
    background: var(--ink);
    margin-right: 12px;
    vertical-align: middle;
  }
  .brand__collection {
    font-size: 13px;
    letter-spacing: 0.5px;
    margin-top: 2px;
  }
  .brand__est {
    font-size: 9px;
    letter-spacing: 3px;
    margin-top: 2px;
  }
  .card--back .brand {
    position: absolute;
    top: 54px;
    left: 0;
    right: 0;
  }
  .contact-list {
    position: absolute;
    left: 34px;
    top: 150px;
    list-style: none;
  }
  .contact-list li {
    display: flex;
    align-items: center;
    gap: 10px;
    font-size: 17px;
    line-height: 34px;
    color: var(--ink);
  }
  .contact-list svg {
    flex: none;
  }

  /* Front of card */
  .card--front {
    left: 560px;
    top: 500px;
    background: linear-gradient(180deg, var(--card-front) 0%, var(--card-front-deep) 100%);
  }
  .card--front .brand {
    position: absolute;
    top: 44px;
    left: 0;
    right: 0;
  }
  .name-band {
    position: absolute;
    left: 0;
    right: 0;
    top: 142px;
    height: 86px;
    background: var(--band);
    display: flex;
    align-items: center;
    justify-content: center;
    gap: 22px;
  }
  .name-band__name {
    font-size: 26px;
    letter-spacing: 1px;
    text-transform: uppercase;
  }
  .name-band__title {
    font-size: 15px;
    color: var(--ink-soft);
    align-self: flex-start;
    margin-top: 18px;
  }
  .tagline {
    position: absolute;
    left: 0;
    right: 0;
    bottom: 40px;
    text-align: center;
    font-size: 15px;
    letter-spacing: 6px;
    text-transform: uppercase;
    color: var(--ink-muted);
  }
</style>
</head>
<body>
<main class="stage">

  <section class="card card--back" aria-label="Back of business card">
    <div class="brand">
      <p class="brand__name">Designs by L&amp;M</p>
      <p class="brand__collection">Renata Kowalczyk Signature Collection</p>
      <p class="brand__est">EST. 2014</p>
    </div>
    <ul class="contact-list">
      <li>
        <svg width="22" height="22" viewBox="0 0 22 22" aria-hidden="true">
          <circle cx="11" cy="11" r="11" fill="var(--ink)"/>
          <rect x="5" y="7" width="12" height="8" fill="none" stroke="var(--card-back)" stroke-width="1.4"/>
          <path d="M5 7 L11 12 L17 7" fill="none" stroke="var(--card-back)" stroke-width="1.4"/>
        </svg>
        LMDesigns27@postvela.com
      </li>
      <li>
        <svg width="22" height="22" viewBox="0 0 22 22" aria-hidden="true"><circle cx="11" cy="11" r="11" fill="var(--ink)"/></svg>
        /chirpline-example.com/DesignsbyLM27
      </li>
      <li>
        <svg width="22" height="22" viewBox="0 0 22 22" aria-hidden="true"><circle cx="11" cy="11" r="11" fill="var(--ink)"/></svg>
        picstream-example.com/DesignsbyLMjewelry
      </li>
      <li>
        <svg width="22" height="22" viewBox="0 0 22 22" aria-hidden="true"><circle cx="11" cy="11" r="11" fill="var(--ink)"/></svg>
        facepage-example.com/DesignsbyLMRenataandHolly
      </li>
    </ul>
  </section>

  <section class="card card--front" aria-label="Front of business card">
    <div class="brand">
      <p class="brand__name">Designs by L&amp;M</p>
      <p class="brand__collection">Renata Kowalczyk Signature Collection</p>
      <p class="brand__est">EST. 2014</p>
    </div>
    <div class="name-band">
      <span class="name-band__name">Holly Brennan</span>
      <span class="name-band__title">owner</span>
    </div>
    <p class="tagline">One of a kind designs for you!</p>
  </section>

</main>
</body>
</html>
```